Varnholt Construction LTD is in need of a web page we are renovation and maintenance specialists

We are a medium size building company specialising in renovations and maintainance on commercial and residential properties bathrooms, kitchens, alterations, commercial shop fit outs, office fit outs. we also specialise in project management taking care of all manners of trades from concept to completion with trade qualified LBP registered builders customers can be assured that they will get the best possible results

Building

2 page

```html
<!DOCTYPE html>
<html lang="en">
<head>
<meta charset="utf-8">
<title>Varnholt Construction LTD</title>
<link href="https://fonts.googleapis.com/css2?family=Open+Sans:wght@400;600;700;800&display=swap" rel="stylesheet">
<style>
:root{
  --navy:#1c2b57;
  --navy-deep:#15214a;
  --blue:#2b4c93;
  --sky:#3d6fc2;
  --grey-bg:#eef0f3;
  --line:#d3d7de;
  --text:#4a4f59;
  --white:#ffffff;
}
*{box-sizing:border-box;margin:0;padding:0}
html,body{width:1200px;height:2704px;overflow:hidden}
body{font-family:"Open Sans",Arial,sans-serif;color:var(--text);background:var(--white);position:relative}
a{color:inherit;text-decoration:none}

/* header */
.site-header{position:absolute;left:0;top:0;width:1200px;height:152px;background:var(--white)}
.brand{position:absolute;left:40px;top:14px;display:flex;align-items:center;gap:14px}
.brand-mark{width:26px;height:26px;background:var(--navy)}
.brand-name{font-weight:800;font-size:30px;color:var(--navy);line-height:1.05;letter-spacing:1px;width:300px}
.top-contact{position:absolute;right:56px;top:38px;display:flex;gap:40px;font-size:15px;color:var(--navy);font-weight:600}
.top-contact span{display:flex;align-items:center;gap:10px}
.main-nav{position:absolute;left:368px;right:0;top:112px;height:36px;background:var(--navy);display:flex;align-items:center;gap:34px;padding-left:18px;font-size:15px;color:var(--white);font-weight:600}
.main-nav a.active{background:var(--sky);padding:8px 14px}

.hero{position:absolute;left:0;top:152px;width:1200px;height:488px;background:linear-gradient(100deg,#e9eef0 0%,#cfd9dc 35%,#f4f6f6 55%,#b9c6c2 80%,#dfe6e3 100%)}

/* services */
.services{position:absolute;left:0;top:640px;width:1200px;height:560px;background:var(--grey-bg)}
.section-title{text-align:center;font-size:40px;font-weight:400;letter-spacing:1px}
.services .section-title{margin-top:40px;color:var(--navy)}
.title-rule{width:90px;height:3px;background:var(--sky);margin:12px auto 0}
.service-card{position:absolute;top:120px;width:328px;height:380px;filter:drop-shadow(0 0 2px rgba(0,0,0,.25))}
.service-card-inner{width:100%;height:100%;background:var(--white);clip-path:polygon(0 0,100% 0,100% 82%,50% 100%,0 82%);padding:16px}
.service-photo{height:124px;background:linear-gradient(120deg,#c9d6e6,#6f8fb9 60%,#3f5f92)}
.service-title{margin-top:22px;font-size:17px;font-weight:700;color:var(--blue)}
.service-text{margin-top:10px;font-size:14px;line-height:1.4}
.read-more{display:block;margin-top:10px;font-size:14px;font-weight:700;color:var(--navy)}

/* projects */
.projects{position:absolute;left:0;top:1200px;width:1200px;height:912px;background:var(--navy)}
.projects .section-title{margin-top:36px;color:var(--white)}
.project-tabs{position:absolute;top:130px;left:0;width:1200px;height:110px}
.tab{position:absolute;width:104px;height:104px;border-radius:50%;border:4px solid #c9ced8;background:radial-gradient(circle,#e6e9ee,#a5adbd);display:flex;align-items:center;justify-content:center;font-size:11px;font-weight:800;color:var(--white);text-align:center;text-shadow:0 1px 2px rgba(0,0,0,.5)}
.tab.active::after{content:"";position:absolute;bottom:-32px;left:36px;border:16px solid transparent;border-bottom-color:var(--white)}
.gallery{position:absolute;left:128px;top:260px;width:944px;height:620px;background:var(--white)}
.gallery-main{position:absolute;left:40px;top:52px;width:864px;height:320px;background:linear-gradient(90deg,#cfd2d4,#f1f2f2 45%,#dfe3e5 70%,#c4c9cc)}
.thumb{position:absolute;top:404px;width:200px;height:156px}
.arrow{position:absolute;top:440px}

/* specialise */
.specialise{position:absolute;left:0;top:2112px;width:1200px;height:336px;background:var(--white)}
.team-photo{position:absolute;left:80px;top:16px;width:512px;height:320px;background:linear-gradient(90deg,#dfe3ea,#2d3446 30%,#e8eaee 50%,#2b3143 75%,#e3e6ec)}
.specialise-copy{position:absolute;left:608px;top:60px;width:520px;font-size:20px;line-height:1.4;color:var(--text)}
.specialise-copy strong{color:var(--blue);font-weight:700}
.specialise-copy .lead{font-size:28px;font-weight:700;color:var(--blue)}
.call-button{position:absolute;left:608px;top:216px;width:500px;height:52px;background:var(--navy);display:flex;align-items:center;padding:0 18px;gap:12px;color:var(--white);font-size:15px;font-weight:600}
.call-button b{font-size:28px;margin-left:auto}

/* footer */
.site-footer{position:absolute;left:0;top:2448px;width:1200px;height:212px;background:var(--navy)}
.footer-col{position:absolute;top:24px;color:var(--white)}
.footer-col h3{font-size:15px;font-weight:700;letter-spacing:.5px;margin-bottom:10px}
.footer-col ul{list-style:none;font-size:12px;line-height:20px;color:#c8cee0}
.footer-col li::before{content:"› ";color:var(--sky)}
.contact-list li::before,.social-list li::before{content:none}
.contact-list li,.social-list li{display:flex;align-items:center;gap:10px;margin-bottom:6px}
.dot{width:18px;height:18px;border-radius:50%;background:#3b5aa0;flex:none}
.footer-brand{position:absolute;left:928px;top:40px;display:flex;align-items:center;gap:12px;width:240px}
.footer-brand .brand-mark{background:var(--sky)}
.footer-brand .brand-name{color:var(--sky);font-size:24px;width:auto}
.copyright{position:absolute;left:0;top:2660px;width:1200px;height:44px;background:var(--navy-deep);color:#9aa4c0;font-size:12px;display:flex;align-items:center;justify-content:center}
</style>
</head>
<body>

<header class="site-header">
  <div class="brand"><span class="brand-mark"></span><span class="brand-name">VARNHOLT CONSTRUCTION LIMITED</span></div>
  <div class="top-contact">
    <span><svg width="18" height="13" viewBox="0 0 18 13"><rect x="1" y="1" width="16" height="11" fill="none" stroke="#1c2b57" stroke-width="2"/><path d="M1 1l8 6 8-6" fill="none" stroke="#1c2b57" stroke-width="2"/></svg>info@varnholtbuild.com</span>
    <span><svg width="16" height="16" viewBox="0 0 16 16"><path d="M3 1l3 3-2 2c1 2 3 4 5 5l2-2 3 3-2 3C7 14 2 9 1 3z" fill="#1c2b57"/></svg>1-800-555-0142</span>
  </div>
  <nav class="main-nav">
    <a class="active">HOME</a><a>ABOUT US</a><a>COMMERCIAL SERVICES</a><a>RESIDENTIAL SERVICES</a><a>GALLERY</a><a>CONTACT US</a>
  </nav>
</header>

<div class="hero" role="img" aria-label="Bright renovated kitchen with white island, bar stools and garden doors"></div>

<section class="services">
  <h2 class="section-title">OUR SERVICES</h2>
  <div class="title-rule"></div>

  <article class="service-card" style="left:88px"><div class="service-card-inner">
    <div class="service-photo" role="img" aria-label="Tradesman working on a renovation"></div>
    <h3 class="service-title">REMODELING/RENOVATIONS</h3>
    <p class="service-text">We rework bathrooms, kitchens and living areas with care, planning every stage so your home is ready on time and on budget.</p>
    <a class="read-more">READ MORE...</a>
  </div></article>

  <article class="service-card" style="left:436px"><div class="service-card-inner">
    <div class="service-photo" role="img" aria-label="Technician servicing building equipment"></div>
    <h3 class="service-title">MAINTANANCE</h3>
    <p class="service-text">Regular upkeep and quick repairs for homes and shops, keeping your property safe, sound and looking its best all year round.</p>
    <a class="read-more">READ MORE...</a>
  </div></article>

  <article class="service-card" style="left:800px"><div class="service-card-inner">
    <div class="service-photo" role="img" aria-label="Builders in hard hats on a commercial site"></div>
    <h3 class="service-title">COMMERCIAL &amp; RESIDENTIAL</h3>
    <p class="service-text">Shop and office fit outs plus home projects, run by qualified builders who manage every trade from concept to completion.</p>
    <a class="read-more">READ MORE...</a>
  </div></article>
</section>

<section class="projects">
  <h2 class="section-title">OUR PROJECTS</h2>
  <div class="project-tabs">
    <div class="tab active" style="left:196px">BATHROOMS</div>
    <div class="tab" style="left:376px">KITCHENS</div>
    <div class="tab" style="left:548px">ALTERATIONS</div>
    <div class="tab" style="left:720px">SHOP FIT OUTS</div>
    <div class="tab" style="left:896px">OFFICE FIT OUTS</div>
  </div>
  <div class="gallery">
    <div class="gallery-main" role="img" aria-label="Finished bathroom with freestanding bath and tall windows"></div>
    <div class="thumb" style="left:40px;background:linear-gradient(135deg,#3b3a3a,#8d8a86)" role="img" aria-label="Dark tiled bathroom vanity"></div>
    <div class="thumb" style="left:262px;background:linear-gradient(135deg,#e4e6e8,#9aa3aa)" role="img" aria-label="Modern bathroom with shower"></div>
    <div class="thumb" style="left:484px;background:linear-gradient(135deg,#f0f1f1,#c5cacd)" role="img" aria-label="White bathroom with basin"></div>
    <div class="thumb" style="left:704px;background:linear-gradient(135deg,#eef0f1,#6b6f74)" role="img" aria-label="Clawfoot bath in bright room"></div>
    <svg class="arrow" style="left:10px" width="20" height="36" viewBox="0 0 20 36"><path d="M16 2L4 18l12 16" fill="none" stroke="#9aa0aa" stroke-width="3"/></svg>
    <svg class="arrow" style="right:10px" width="20" height="36" viewBox="0 0 20 36"><path d="M4 2l12 16L4 34" fill="none" stroke="#9aa0aa" stroke-width="3"/></svg>
  </div>
</section>

<section class="specialise">
  <div class="team-photo" role="img" aria-label="Team of builders in white hard hats reviewing plans"></div>
  <p class="specialise-copy"><span class="lead">We specialise</span> in project management taking care of all manners of trades from concept to completion with trade qualified <strong>LBP registered builders.</strong> Customers can be assured that they will get the best possible results.</p>
  <div class="call-button">
    <svg width="20" height="20" viewBox="0 0 16 16"><path d="M3 1l3 3-2 2c1 2 3 4 5 5l2-2 3 3-2 3C7 14 2 9 1 3z" fill="#3d6fc2"/></svg>
    CALL NOW TO GET BEST RESULTS <b>890-555-0187</b>
  </div>
</section>

<footer class="site-footer">
  <div class="footer-col" style="left:80px">
    <h3>QUICK LINKS</h3>
    <ul><li>Home</li><li>About Us</li><li>Commercial Services</li><li>Residential Services</li><li>Gallery</li><li>Contact Us</li></ul>
  </div>
  <div class="footer-col" style="left:368px">
    <h3>QUICK CONTACT</h3>
    <ul class="contact-list">
      <li><span class="dot"></span>VCL Property Services, 12 Kiln Road, Eastbrook</li>
      <li><span class="dot"></span>1-800-555-0142</li>
      <li><span class="dot"></span>info@varnholtbuild.com</li>
    </ul>
  </div>
  <div class="footer-col" style="left:700px">
    <h3>SOCIAL NETWORKING</h3>
    <ul class="social-list">
      <li><span class="dot"></span>Community Page</li>
      <li><span class="dot"></span>News Feed</li>
      <li><span class="dot"></span>Business Network</li>
    </ul>
  </div>
  <div class="footer-brand"><span class="brand-mark"></span><span class="brand-name">VARNHOLT CONSTRUCTION</span></div>
</footer>
<div class="copyright">Copyright © 2017 Varnholt Construction Limited. All rights reserved.</div>

</body>
</html>
```